Healthcare IT company looking for business card design

We develop IT systems for healthcare that significantly reduces cost and improves quality.

We want a business card design that is professional and clean, and using the colors in our logo.

Target Market(s)

Doctors and decision makers in the healthcare industry

Industry/Entity Type

Healthcare

Contact Information for Business Card

It should include
Name and title, address, telephone

Tobias Vrenholt, CEO
+46 712 418257
tobias@kelvaro.se

Font styles to use
Serif

Colors
0355a3
ed282f

Requirements
Must have
• Clean design
• Professional feel
Nice to have
• N/A
Should not have
• N/A

```html
<!DOCTYPE html>
<html lang="en">
<head>
<meta charset="utf-8">
<title>Kelvaro business card</title>
<link rel="stylesheet" href="https://fonts.googleapis.com/css2?family=Source+Sans+3:wght@400;600;700&display=swap">
<style>
  :root {
    --brand-blue: #0355a3;
    --brand-red: #ed282f;
    --soft-red: #fbdcdd;
    --card-white: #ffffff;
    --ink: #1f1f1f;
    --edge: #3a3a3a;
    --backdrop: #efebe5;
  }
  * { margin: 0; padding: 0; box-sizing: border-box; }
  html, body {
    width: 1200px; height: 1114px; overflow: hidden;
    background: var(--backdrop);
    font-family: "Source Sans 3", "Myriad Pro", Arial, sans-serif;
  }
  .canvas { position: relative; width: 1200px; height: 1114px; }

  .card {
    position: absolute;
    width: 811px; height: 463px;
    background: var(--card-white);
    border: 1.5px solid var(--edge);
    border-radius: 46px;
    overflow: hidden;
  }
  .card--front { left: 62px; top: 72px; }
  .card--back  { left: 313px; top: 591px; }

  .accent-tab {
    position: absolute; left: 0; top: 63px;
    width: 16px; height: 50px; background: var(--brand-red);
  }
  .holder-name {
    position: absolute; left: 34px; top: 56px;
    font-size: 29px; font-weight: 700; color: var(--brand-blue);
  }
  .holder-title {
    position: absolute; left: 34px; top: 91px;
    font-size: 23px; font-weight: 400; color: var(--brand-red);
  }
  .wordmark {
    position: absolute;
    font-weight: 700; color: var(--brand-blue);
    letter-spacing: -0.01em; line-height: 1;
  }
  .card--front .wordmark { right: 32px; top: 28px; font-size: 112px; }
  .card--back .wordmark {
    left: 0; right: 0; top: 140px; text-align: center; font-size: 156px;
  }
  .faint-disc {
    position: absolute; border-radius: 50%; background: var(--soft-red);
  }
  .card--front .faint-disc { left: 588px; top: 184px; width: 206px; height: 206px; }
  .card--back .faint-disc { left: 218px; top: 40px; width: 380px; height: 380px; }

  .contact-list {
    position: absolute; left: 32px; top: 308px; list-style: none;
    font-size: 20px; color: var(--ink);
  }
  .contact-list li { display: flex; align-items: center; height: 32px; }
  .contact-list svg { width: 16px; height: 16px; margin-right: 10px; }

  .footer-bands { position: absolute; left: 0; top: 398px; width: 811px; height: 65px; }
  .footer-url {
    position: absolute; left: 32px; top: 402px;
    font-size: 21px; letter-spacing: 0.22em; color: var(--card-white);
  }
  .back-url {
    position: absolute; left: 0; right: 0; top: 383px; text-align: center;
    font-size: 24px; letter-spacing: 0.22em; color: var(--ink);
  }
</style>
</head>
<body>
<main class="canvas">
  <section class="card card--front">
    <span class="accent-tab"></span>
    <h1 class="holder-name">Tobias Vrenholt</h1>
    <p class="holder-title">CEO</p>
    <span class="faint-disc"></span>
    <p class="wordmark">Kelvaro</p>
    <ul class="contact-list">
      <li>
        <svg viewBox="0 0 16 16"><circle cx="8" cy="8" r="7" fill="none" stroke="#0355a3" stroke-width="1.5"/><path d="M5.5 4.5l1.5 0 .6 2-1 .8a5 5 0 0 0 2.1 2.1l.8-1 2 .6v1.5c-3.5.3-6.3-2.5-6-6z" fill="#0355a3"/></svg>
        +46 712 418257
      </li>
      <li>
        <svg viewBox="0 0 16 16"><path d="M1 6l7-4 7 4v8H1z" fill="#0355a3"/><path d="M3 7l5 3 5-3" fill="none" stroke="#fff" stroke-width="1.3"/></svg>
        tobias@kelvaro.se
      </li>
    </ul>
    <svg class="footer-bands" viewBox="0 0 811 65" preserveAspectRatio="none">
      <rect x="0" y="0" width="811" height="65" fill="#0355a3"/>
      <path d="M0 2H548C535 8 528 24 515 35H0Z" fill="#ed282f"/>
    </svg>
    <p class="footer-url">www.kelvaro.com</p>
  </section>

  <section class="card card--back">
    <span class="faint-disc"></span>
    <p class="wordmark">Kelvaro</p>
    <p class="back-url">www.kelvaro.com</p>
  </section>
</main>
</body>
</html>
```